Author needs eye catching business card design

I need a design that depicts an item from my book Vessen. This item is a blue stone that houses a dragon soul in it. You can vaguely see the shape of a dragon spiraling around the stone in a shimmering blue-silver hue. I've attached my concept design. I've also attached a bookmark concept design to help inspire. I also have attached a picture of a stone that is the color that the stones in my book are. On the back I would like something nice looking but blank for the most part - a space for me to write on if I want. On the front of the card I would like the following stacked upon each other : Fantasy Author, Della Korvane, www.dkorvane.com

Contact Information for Business Card

Font styles to use
Serif
Script

Requirements
Must have
• 1 Dragon wisp swirling around inside the stone. I have attached my concept drawing for inspiration.
• The following text stacked upon each other: Fantasy Author, Della Korvane, www.dkorvane.com, d_korvane@mailvey.com
• The symbols for Tackboard, Photovyne, Kinspace, and Chirrup followed by "@dellabkorvane"
Should not have
• The exact picture of the stone picture I have attached. This is for color and size/shape inspiration only and is not my own personal picture.
• No pink please.

```html
<!DOCTYPE html>
<html lang="en">
<head>
<meta charset="utf-8">
<title>Della Korvane – Business Card</title>
<link rel="stylesheet" href="https://fonts.googleapis.com/css2?family=Open+Sans:wght@400;600;700&display=swap">
<style>
  :root {
    --page: #ecebea;
    --card-white: #ffffff;
    --navy: #1f2a6b;
    --ink: #2a2d45;
    --violet: #5a2f93;
    --violet-deep: #3b2a9a;
    --cyan: #17b6ec;
    --sky: #7fd3f5;
    --indigo: #2d1f8f;
  }
  * { margin: 0; padding: 0; box-sizing: border-box; }
  html, body {
    width: 1200px; height: 1000px; overflow: hidden;
    background: var(--page);
    font-family: "Open Sans", Arial, sans-serif;
  }
  .canvas { position: relative; width: 1200px; height: 1000px; }

  .card {
    position: absolute;
    width: 670px; height: 398px;
    border-radius: 22px;
    overflow: hidden;
    background: var(--card-white);
    box-shadow: 0 3px 10px rgba(0,0,0,0.18);
  }
  .card--front { left: 262px; top: 73px; }
  .card--back  { left: 264px; top: 533px; height: 397px; }

  .wash { position: absolute; inset: 0; }
  .card--front .wash {
    background:
      radial-gradient(ellipse 120px 160px at 20px 90px, rgba(59,42,154,0.85), transparent 80%),
      radial-gradient(ellipse 170px 120px at 40px 380px, rgba(23,182,236,0.85), transparent 80%),
      radial-gradient(ellipse 220px 160px at 260px 420px, rgba(127,211,245,0.8), transparent 75%),
      radial-gradient(ellipse 140px 90px at 200px 10px, rgba(90,47,147,0.45), transparent 80%),
      radial-gradient(ellipse 160px 200px at 150px 200px, rgba(127,211,245,0.35), transparent 80%),
      var(--card-white);
  }
  .stone-art {
    position: absolute; left: 330px; top: -10px; width: 360px; height: 420px;
  }

  .details { position: absolute; left: 45px; top: 133px; color: var(--ink); }
  .details__name {
    font-size: 23px; font-weight: 700; color: var(--navy); letter-spacing: 0.3px; line-height: 1;
  }
  .details__role { font-size: 17px; margin-top: 5px; color: var(--ink); }
  .contact { margin-top: 22px; list-style: none; }
  .contact__item {
    display: flex; align-items: center; gap: 7px;
    font-size: 17px; line-height: 25px; color: var(--ink);
  }
  .contact__icon { width: 15px; height: 15px; flex: none; }
  .social { margin-top: 9px; }
  .social__networks { display: flex; gap: 6px; list-style: none; }
  .social__network {
    display: flex; align-items: center; gap: 3px;
    font-size: 9px; font-weight: 600; color: var(--violet); white-space: nowrap;
  }
  .social__dot { width: 6px; height: 6px; border-radius: 50%; background: var(--violet); }
  .social__handle { font-size: 18px; font-weight: 600; color: var(--violet); margin-top: 2px; }

  .card--back .wash {
    background:
      radial-gradient(ellipse 140px 120px at 600px 40px, rgba(59,42,154,0.9), transparent 80%),
      radial-gradient(ellipse 200px 260px at 640px 250px, rgba(23,182,236,0.9), transparent 75%),
      radial-gradient(ellipse 220px 140px at 480px 400px, rgba(127,211,245,0.75), transparent 80%),
      radial-gradient(ellipse 160px 200px at 430px 170px, rgba(127,211,245,0.3), transparent 80%),
      var(--card-white);
  }
  .dragon-art {
    position: absolute; inset: 0;
    background:
      radial-gradient(ellipse 230px 330px at 70px 170px,
        rgba(45,31,143,0.95) 0%,
        rgba(90,47,147,0.9) 30%,
        rgba(23,182,236,0.85) 62%,
        rgba(127,211,245,0.4) 82%,
        rgba(255,255,255,0) 100%);
  }
</style>
</head>
<body>
<main class="canvas">

  <section class="card card--front" aria-label="Business card front">
    <div class="wash"></div>
    <svg class="stone-art" viewBox="0 0 360 420" role="img" aria-label="Illustration of glossy blue stones with a dragon spiralling around them">
      <defs>
        <radialGradient id="stoneBack" cx="0.6" cy="0.4" r="0.7">
          <stop offset="0" stop-color="#5a2f93"/>
          <stop offset="1" stop-color="#2d1f8f"/>
        </radialGradient>
        <linearGradient id="stoneFront" x1="0" y1="0" x2="0" y2="1">
          <stop offset="0" stop-color="#5a2f93"/>
          <stop offset="0.45" stop-color="#3b2a9a"/>
          <stop offset="0.75" stop-color="#17b6ec"/>
          <stop offset="1" stop-color="#7fd3f5"/>
        </linearGradient>
      </defs>
      <ellipse cx="270" cy="170" rx="110" ry="190" fill="url(#stoneBack)" opacity="0.85"/>
      <ellipse cx="140" cy="250" rx="90" ry="150" fill="#2f6fd8" opacity="0.7"/>
      <ellipse cx="120" cy="205" rx="88" ry="192" fill="url(#stoneFront)"/>
    </svg>
    <div class="details">
      <h1 class="details__name">DELLA KORVANE</h1>
      <p class="details__role">Fantasy Author</p>
      <ul class="contact">
        <li class="contact__item">
          <svg class="contact__icon" viewBox="0 0 16 16" aria-hidden="true"><rect x="1" y="3.5" width="14" height="9" fill="#2a2d45"/><path d="M1.5 4l6.5 5 6.5-5" fill="none" stroke="#fff" stroke-width="1.2"/></svg>
          d_korvane@mailvey.com
        </li>
        <li class="contact__item">
          <svg class="contact__icon" viewBox="0 0 16 16" aria-hidden="true"><circle cx="8" cy="8" r="6.5" fill="none" stroke="#2a2d45" stroke-width="1.6"/><path d="M1.5 8h13M8 1.5c-3 3-3 10 0 13M8 1.5c3 3 3 10 0 13" fill="none" stroke="#2a2d45" stroke-width="1.1"/></svg>
          www.dkorvane.com
        </li>
      </ul>
      <div class="social">
        <ul class="social__networks">
          <li class="social__network"><span class="social__dot"></span>Photovyne</li>
          <li class="social__network"><span class="social__dot"></span>Chirrup</li>
          <li class="social__network"><span class="social__dot"></span>Kinspace</li>
          <li class="social__network"><span class="social__dot"></span>Scrollnest</li>
          <li class="social__network"><span class="social__dot"></span>Tackboard</li>
        </ul>
        <p class="social__handle">@dellabkorvane</p>
      </div>
    </div>
  </section>

  <section class="card card--back" aria-label="Business card back">
    <div class="wash"></div>
    <div class="dragon-art" role="img" aria-label="Watercolor dragon coiling in the top left corner, with faint feathers drifting across the card"></div>
  </section>

</main>
</body>
</html>
```